Brightwell has a great new logo - now we need a website!!

Brightwell has been in business for a long time and needs to start a new era. Additional to other changes being made in the business itself, Brightwell needs an overhaul of its entire branding. PART 1 is COMPLETE - we have our new logo!

Next step... new website! That's where you come in.

Brightwell provides a range of computer related services including computer maintenance, networking, sales & cloud services. We provide onsite (field) and remote support. Our customers range from homes to companies with 100+ computers. We pride ourselves on clear and honest communication.

We are a small business but want a professional yet easy-going look that shows the 'cool' side of having your computer system cared for. The website should exude trustworthiness and professionalism but still get comments like 'modern' and 'smart design'. We want our customers to feel that choosing any other company to maintain their system would be a 'geeky' choice.

We like clear thinking so an uncluttered, well organised structure is appreciated. Obvious references to calling or emailing us would be good so people dont need to search around for our contact details.

We look after both Orvane & Kelvantix operating systems so there needs to be universal appeal rather than a look associated with only one of these two brands.

We want to wow our current clients but also attract new ones so a focus on SEO is a must. And a focus on social media too with links/feeds to Chatterloop, blipcast and Workweave!

Have a look at www.brightwell-tech.com.au so you can see for yourself how much you can help us!

**Breathe new life into Brightwell's online presence!**

(We do have a separate website www.hubloomdesk.com.au that we set as the homepage for our clients - we like how it is but it might need freshening up to match our new site. We will also want our chatterloop page totally made over. You'll probably have other suggestions of things we should be doing. We want to form an ongoing relationship with the right designer!)

(Also, we are open to suggestions regarding the logo size and colour)
Updates

I dont want to cramp anyones creativity but i like this: http://www.quandrelweb.com/demo/themes/wordpress/2011/pebble/

I'm obivously happy to see your own ideas too!

I also like this one: http://layoutmarkt.net/item/zindo-responsive-wordpress-theme/7718205

Clarification: We are looking for a working, implemented website, not just design of the theme. Once the general page layout is done we can do the majority of the content input. But we do want a workable shell with images.

We are open to buying existing themes if that helps. Thanks!

Site also needs email contact form, testimonial submission page, blog (feed to home page), chatterloop like button

Reason: I haven't found the ideal one yet... We want some other designers to send their ideas.

Reason: We need a little more time to make our decision.

Target Market(s)

Mainly small to medium businesses but also homes

Industry/Entity Type

Small Business

Requirements
Must have
• SEO
Social Media
That little address bar icon
R in a circle at the bottom of the site to show we have trademarked our company name
A finished product website with content and images that we can modify ourselves over time.

```html
<!DOCTYPE html>
<html lang="en">
<head>
<meta charset="utf-8">
<title>Brightwell IT Solutions &amp; Support</title>
<link href="https://fonts.googleapis.com/css2?family=Lato:wght@300;400;700&family=Ubuntu:wght@400;500;700&family=Fredoka:wght@500;600&display=swap" rel="stylesheet">
<style>
:root{
  --navy:#173e6e;
  --navy-dark:#0f2d55;
  --blue:#2a5f9c;
  --nav-top:#4d7fbd;
  --nav-bot:#2c5b94;
  --ink:#333;
  --muted:#555;
  --link:#2c78b8;
  --heading:#1f4c86;
  --paper:#ececec;
  --paper-dark:#dedede;
  --card-rim:#e2e2e2;
  --orange:#f39a1d;
  --orange-dark:#e07a0b;
}
*{box-sizing:border-box;margin:0;padding:0}
html,body{width:1029px;height:1200px;overflow:hidden;background:var(--paper)}
body{font-family:"Lato",sans-serif;color:var(--ink)}
.stage{position:relative;width:1029px;height:1200px;overflow:hidden;background:var(--paper)}
.abs{position:absolute}
a{color:inherit;text-decoration:none}

/* header */
.brand{left:100px;top:26px;display:flex;align-items:center;gap:10px}
.brand-dot{width:62px;height:62px;border-radius:50%;background:var(--navy)}
.brand-name{font-family:"Ubuntu",sans-serif;font-weight:700;font-size:30px;color:#2b2b2b;line-height:1}
.brand-sub{font-family:"Lato",sans-serif;font-size:15px;color:#555;margin-top:2px}
.nav{left:390px;top:48px;width:546px;height:39px;border-radius:6px;display:flex;overflow:hidden;
  background:linear-gradient(var(--nav-top),var(--nav-bot));box-shadow:0 1px 3px rgba(0,0,0,.35)}
.nav-home{width:50px;background:linear-gradient(#444,#1c1c1c);display:flex;align-items:center;justify-content:center}
.nav a{flex:1;display:flex;align-items:center;justify-content:center;color:#fff;font-size:12px;border-left:1px solid rgba(0,0,0,.25)}
.tagline{left:0;top:105px;width:1029px;height:47px;background:linear-gradient(#2a5a93,#1c4679);
  color:#d7e3f2;font-weight:300;font-size:19px;text-align:center;line-height:47px;border-bottom:1px solid #123463}
.tagline::before{content:"";position:absolute;left:0;top:-3px;width:100%;height:4px;background:repeating-linear-gradient(90deg,#2a5a93 0 6px,transparent 6px 10px)}

/* hero */
.hero{left:0;top:152px;width:1029px;height:291px;background:linear-gradient(var(--navy),var(--navy-dark))}
.hero-frame{left:109px;top:177px;width:387px;height:239px;background:#fff;box-shadow:0 6px 10px rgba(0,0,0,.4)}
.hero-photo{left:119px;top:188px;width:366px;height:216px;background:linear-gradient(100deg,#6fa6d8 0%,#2d5e97 45%,#111 70%,#0b0b0b 100%)}
.hero-kicker{right:104px;top:172px;font-family:"Ubuntu",sans-serif;font-weight:700;font-size:22px;color:#fff}
.hero-title{left:517px;top:210px;width:411px;text-align:right;white-space:nowrap;font-family:"Fredoka",sans-serif;font-weight:600;font-size:27px;line-height:34px;color:#fff;text-shadow:0 2px 3px rgba(0,0,0,.5)}
.hero-copy{left:518px;top:272px;width:407px;font-family:Arial,sans-serif;font-size:11px;line-height:17px;color:#fff;text-align:justify}
.btn-read{left:820px;top:365px;width:105px;height:36px;border-radius:5px;border:2px solid #fff;
  background:linear-gradient(#ffb23c,var(--orange-dark));font-family:"Ubuntu",sans-serif;font-weight:700;font-size:15px;color:#3a1d00;
  display:flex;align-items:center;justify-content:center}

/* feature cards */
.feat-head{top:466px;display:flex;align-items:center;gap:10px;font-family:"Ubuntu",sans-serif;font-weight:700;font-size:18px;color:var(--heading)}
.feat-icon{width:28px;height:28px;border-radius:6px}
.card{top:505px;width:259px;height:235px;background:var(--card-rim);border-radius:8px}
.card-inner{position:absolute;left:7px;top:7px;right:7px;bottom:7px;background:#fafafa;border-radius:6px;box-shadow:0 1px 3px rgba(0,0,0,.15)}
.card-img{position:absolute;left:12px;top:11px;width:222px;height:106px}
.card-text{position:absolute;left:12px;top:128px;width:222px;font-size:12px;line-height:15.5px;text-align:justify;color:#333}
.card-more{position:absolute;right:12px;top:199px;font-size:11px;color:var(--heading)}

.divider{left:98px;top:774px;width:832px;height:1px;background:#cfcfcf}
.vrule{top:800px;height:195px;border-left:1px dotted #aaa}

/* section pills */
.pill{top:790px;width:188px;height:36px;border-radius:18px;background:linear-gradient(#fff,#d8d8d8);box-shadow:0 1px 3px rgba(0,0,0,.35);display:flex;align-items:center;padding:3px}
.pill-icon{width:30px;height:30px;border-radius:50%;flex:none}
.pill-label{margin-left:8px;flex:1;height:22px;border-radius:11px;background:linear-gradient(#dcdcdc,#c8c8c8);
  font-family:"Ubuntu",sans-serif;font-weight:500;font-size:12px;color:var(--heading);display:flex;align-items:center;padding-left:10px}
.welcome{left:107px;top:845px;width:210px;font-size:11px;line-height:17px;text-align:justify;color:#333}

.post{left:392px;width:206px;font-size:10px;color:#333}
.post-meta{color:var(--link);font-size:10.5px}
.post-body{display:flex;gap:8px;margin-top:5px}
.avatar{width:29px;height:29px;background:#8a7f72;flex:none}
.post-text{line-height:12px;text-align:justify}
.post-links{margin:6px 0 0 47px;color:var(--link);font-size:10px}
.post-links a{text-decoration:underline;margin-right:12px}

.field{left:670px;width:207px;border-radius:4px;background:linear-gradient(#e6e6e6,#f2f2f2);border:1px solid #cfcfcf;
  box-shadow:inset 0 1px 2px rgba(0,0,0,.15);font-size:11px;color:#444;padding:8px 11px}
.btn-dark{border-radius:5px;background:linear-gradient(#4b4b4b,#151515);color:#fff;font-family:"Ubuntu",sans-serif;font-weight:500;font-size:12px;
  display:flex;align-items:center;justify-content:center;box-shadow:0 0 0 2px #fff,0 1px 4px 2px rgba(0,0,0,.3)}

/* footer */
.footer{left:0;top:1016px;width:1029px;height:184px;background:var(--paper-dark)}
.foot-title{top:1029px;font-family:"Ubuntu",sans-serif;font-weight:500;font-size:13px;color:var(--heading);letter-spacing:.3px}
.socials{left:109px;top:1058px;display:flex;gap:6px}
.social{width:28px;height:28px;border-radius:50%;box-shadow:0 1px 2px rgba(0,0,0,.4)}
.foot-brand{left:114px;top:1124px;display:flex;align-items:center;gap:8px}
.foot-brand .brand-dot{width:46px;height:46px;background:#555}
.foot-brand .brand-name{font-size:20px;color:#555}
.foot-brand .brand-sub{font-size:11px;color:#777}
.sitemap{left:373px;top:1062px;font-size:12px;color:#333;line-height:19px}
.sitemap span{display:inline-block;margin-right:14px}
.sitemap span::before{content:"";display:inline-block;border-left:4px solid #555;border-top:3px solid transparent;border-bottom:3px solid transparent;margin-right:9px;vertical-align:1px}
.copy{left:398px;top:1152px;width:200px;text-align:center;font-size:11px;line-height:19px;color:#333}
.news-copy{left:671px;top:1049px;width:210px;font-size:11px;line-height:16px;color:#555}
.contact-email{left:701px;top:1146px;font-size:9.5px;color:#222}
.contact-phone{left:670px;top:1158px;display:flex;align-items:center;gap:10px;font-family:"Ubuntu",sans-serif;font-weight:700;font-size:21px;color:#222}
</style>
</head>
<body>
<div class="stage">

  <!-- Header -->
  <div class="abs brand">
    <div class="brand-dot"></div>
    <div><div class="brand-name">Brightwell</div><div class="brand-sub">IT Solutions &amp; Support</div></div>
  </div>
  <nav class="abs nav">
    <div class="nav-home"><svg width="20" height="16" viewBox="0 0 20 16"><path d="M10 1 1 8h3v7h4v-4h4v4h4V8h3z" fill="#fff"/></svg></div>
    <a href="#">Services</a><a href="#">Pricing</a><a href="#">Hours</a><a href="#">Payments</a><a href="#">Links</a><a href="#">News</a><a href="#">Contact</a>
  </nav>
  <div class="abs tagline">Vivamus varius augue sed lacus congue in varius eros volutpat.</div>

  <!-- Hero -->
  <section class="abs hero"></section>
  <div class="abs hero-frame"></div>
  <div class="abs hero-photo" role="img" aria-label="Businessman in a dark suit with arms crossed in a blue office"></div>
  <div class="abs hero-kicker">Complete IT Solutions</div>
  <div class="abs hero-title">SATISFACTION &amp; SUCCESS</div>
  <p class="abs hero-copy">Lorem ipsum dolor sit amet, consectetur adipiscing elit. Quisque id fringilla lacus. Phasellus nulla tellus, tempus scelerisque consequat eget, viverra accumsan lacus. Duis ac faucibus ligula. Vivamus varius augue sed lacus congue in varius eros volutpat. Sed at leo dui, eu malesuada nisi....</p>
  <a class="abs btn-read" href="#">Read More...</a>

  <!-- Features -->
  <div class="abs feat-head" style="left:118px"><div class="feat-icon" style="background:#8aa1bb"></div>Services</div>
  <div class="abs feat-head" style="left:405px"><div class="feat-icon" style="background:#2a9fd0"></div><span style="color:#1f8fc4">Sales</span></div>
  <div class="abs feat-head" style="left:680px"><div class="feat-icon" style="background:#9a9a9a;border-radius:50%"></div><span style="color:#333">Support</span></div>

  <div class="abs card" style="left:103px"><div class="card-inner">
    <div class="card-img" role="img" aria-label="Speakers around a glowing globe on a blue backdrop" style="background:linear-gradient(#7fd0f2,#1d6fb0 60%,#0d2e52)"></div>
    <p class="card-text">Fusce in ligula massa, ac adipiscing felis. Proin dignissim, lorem sit amet facilisis viverra, ante mauris dignissim orci..</p>
    <a class="card-more" href="#">More Details...</a></div></div>
  <div class="abs card" style="left:384px"><div class="card-inner">
    <div class="card-img" role="img" aria-label="Handshake between two computer screens" style="background:linear-gradient(90deg,#1c4d86,#8ec3ea 50%,#1c4d86)"></div>
    <p class="card-text">Fusce in ligula massa, ac adipiscing felis. Proin dignissim, lorem sit amet facilisis viverra, ante mauris dignissim orci..</p>
    <a class="card-more" href="#">More Details...</a></div></div>
  <div class="abs card" style="left:668px"><div class="card-inner">
    <div class="card-img" role="img" aria-label="Support agent wearing a headset at a desk" style="background:linear-gradient(90deg,#c9dcec,#8fb3d4 60%,#5d7fa0)"></div>
    <p class="card-text">Fusce in ligula massa, ac adipiscing felis. Proin dignissim, lorem sit amet facilisis viverra, ante mauris dignissim orci..</p>
    <a class="card-more" href="#">More Details...</a></div></div>

  <div class="abs divider"></div>
  <div class="abs vrule" style="left:353px"></div>
  <div class="abs vrule" style="left:637px"></div>

  <!-- Welcome -->
  <div class="abs pill" style="left:107px"><div class="pill-icon" style="background:radial-gradient(circle at 40% 35%,#7fb3ea,#1f5ea8)"></div><div class="pill-label">Welcome Message</div></div>
  <p class="abs welcome">Lorem ipsum dolor sit amet, consectetur adipiscing elit. Quisque id fringilla lacus. Phasellus nulla tellus, tempus scelerisque consequat eget, viverra accumsan lacus. Duis ac faucibus ligula. Vivamus varius augue sed lacus congue in varius eros volutpat. Sed at leo dui,</p>

  <!-- Feed -->
  <div class="abs pill" style="left:387px"><div class="pill-icon" style="background:radial-gradient(circle at 40% 35%,#8fd8f5,#1a8fc8)"></div><div class="pill-label">Recent Blipcast Feed</div></div>
  <div class="abs post" style="top:851px">
    <div class="post-meta">@marlowen &nbsp;|&nbsp; dated: 02-11-12</div>
    <div class="post-body"><div class="avatar" role="img" aria-label="Member portrait"></div><div class="post-text">Lorem ipsum dolor sit amet, consectetur adipiscing elit. Quisque id fringilla lacus.</div></div>
    <div class="post-links"><a href="#">Reply</a><a href="#">View Post</a></div>
  </div>
  <div class="abs post" style="top:934px">
    <div class="post-meta">@tessavine &nbsp;|&nbsp; dated: 01-11-12</div>
    <div class="post-body"><div class="avatar" role="img" aria-label="Member portrait" style="background:#a08670"></div><div class="post-text">Lorem ipsum dolor sit amet, consectetur adipiscing elit. Quisque id fringilla lacus.</div></div>
    <div class="post-links"><a href="#">Reply</a><a href="#">View Post</a></div>
  </div>

  <!-- Enquiry -->
  <div class="abs pill" style="left:673px"><div class="pill-icon" style="background:radial-gradient(circle at 40% 35%,#bbb,#444)"></div><div class="pill-label">Quick Enquiry</div></div>
  <div class="abs field" style="top:840px;height:28px">Your Name</div>
  <div class="abs field" style="top:874px;height:28px">Your Email</div>
  <div class="abs field" style="top:908px;height:66px">Your Query</div>
  <a class="abs btn-dark" href="#" style="left:813px;top:980px;width:63px;height:23px">Submit</a>

  <!-- Footer -->
  <footer class="abs footer"></footer>
  <div class="abs foot-title" style="left:116px">FOLLOW US ON</div>
  <div class="abs socials">
    <div class="social" style="background:#2f5b9a"></div>
    <div class="social" style="background:#3aa3d9"></div>
    <div class="social" style="background:#2d7eb5"></div>
    <div class="social" style="background:#333"></div>
    <div class="social" style="background:#8a8a8a"></div>
    <div class="social" style="background:#f06a12"></div>
  </div>
  <div class="abs foot-brand">
    <div class="brand-dot"></div>
    <div><div class="brand-name">Brightwell</div><div class="brand-sub">IT Solutions &amp; Support</div></div>
  </div>

  <div class="abs foot-title" style="left:387px">SITEMAP</div>
  <div class="abs sitemap">
    <div><span>Home</span><span>Services</span><span>Pricing</span><span>Hours</span></div>
    <div><span>Payments</span><span>Links</span><span>News</span><span>Contact</span></div>
  </div>
  <div class="abs copy">Copyright&copy;2012-13<br>Brightwell IT Solutions &amp; Support</div>

  <div class="abs foot-title" style="left:670px">SUBSCRIBE NEWSLETTER</div>
  <p class="abs news-copy">Lorem ipsum dolor sit amet, consectetur adipiscing elit.</p>
  <div class="abs field" style="top:1090px;width:159px;height:28px"></div>
  <a class="abs btn-dark" href="#" style="left:836px;top:1091px;width:36px;height:26px">GO</a>
  <div class="abs contact-email"><b>Email:</b> support@brightwell-tech.com.au</div>
  <div class="abs contact-phone">
    <svg width="24" height="24" viewBox="0 0 24 24"><circle cx="12" cy="12" r="11" fill="none" stroke="#222" stroke-width="1.6"/><path d="M8.5 6.5c.6-.6 1.4-.5 1.800.1l1 1.6c.3.5.2 1.1-.2 1.5l-.7.6c.6 1.4 1.6 2.5 3 3.1l.6-.7c.4-.4 1-.5 1.5-.2l1.6 1c.6.4.7 1.2.1 1.8l-.9.9c-.9.9-2.6.6-4.5-.7a13 13 0 0 1-3.3-3.3c-1.3-1.9-1.6-3.6-.7-4.5z" fill="#222"/></svg>
    555-0142-318
  </div>

</div>
</body>
</html>
```